Front book cover for a training course to help bakers get higher prices and sell more wedding cakes.

We need a front cover for a book that will be teaching bakers how to sell wedding cakes to get higher prices and book more orders. It is a business book. Do not make it look like we want brides to read it. Bakers will be judging the cover to see if it is worth their investment to read it. The title is already in the logo, so do not repeat it.

Target Market(s)

Bakers who sell wedding cakes

Industry/Entity Type

Bakery

Colors

Designer to choose colors to be used in the design.

Requirements
Must have
• Must use the logo. Must have author name: Lou Brand. Must have subtitle: Boost Your Prices. Book More Brides. Build Your Empire.
Nice to have
• You are free to be creative. The concept is not to be pretty. It is a business sales and marketing book

```html
<!DOCTYPE html>
<html lang="en">
<head>
<meta charset="utf-8">
<title>Sweet Margin Method – Book Cover</title>
<link rel="stylesheet" href="https://fonts.googleapis.com/css2?family=Montserrat:wght@500;600&family=Playfair+Display:wght@400&display=swap">
<style>
  :root {
    --page: #ffffff;
    --cover-top: #f0527a;
    --cover-mid: #a35569;
    --cover-bottom: #58585a;
    --ink: #ffffff;
    --rule: #e8456f;
  }
  * { margin: 0; padding: 0; box-sizing: border-box; }
  html, body {
    width: 1200px;
    height: 1200px;
    overflow: hidden;
    background: var(--page);
  }
  .book-cover {
    position: absolute;
    left: 221px;
    top: 31px;
    width: 760px;
    height: 1139px;
    background: linear-gradient(180deg, var(--cover-top) 6%, var(--cover-mid) 50%, var(--cover-bottom) 94%);
    color: var(--ink);
  }
  .brand-name {
    position: absolute;
    left: 0;
    right: 0;
    top: 250px;
    text-align: center;
    font-family: "Playfair Display", serif;
    font-weight: 400;
    font-size: 104px;
    line-height: 1.08;
    letter-spacing: -1px;
    color: var(--ink);
  }
  .subtitle {
    position: absolute;
    left: 163px;
    width: 435px;
    top: 770px;
    list-style: none;
    font-family: "Montserrat", sans-serif;
    font-weight: 500;
    font-size: 29px;
    letter-spacing: 5px;
    text-align: center;
  }
  .subtitle li {
    height: 62px;
    line-height: 62px;
    border-bottom: 1.5px solid var(--rule);
  }
  .subtitle li:last-child { border-bottom: none; }
  .author {
    position: absolute;
    left: 0;
    right: 0;
    top: 1022px;
    text-align: center;
    font-family: "Montserrat", sans-serif;
    font-weight: 600;
    font-size: 52px;
    letter-spacing: -1px;
  }
</style>
</head>
<body>
  <main class="book-cover">
    <h1 class="brand-name">Sweet<br>Margin<br>Method</h1>
    <ul class="subtitle">
      <li>BOOST YOUR PRICES</li>
      <li>BOOK MORE BRIDES</li>
      <li>BUILD YOUR EMPIRE</li>
    </ul>
    <p class="author">LOU BRAND</p>
  </main>
</body>
</html>
```